2019 Ignite a Hidden Titan Within (Cardio Calendar)

I would like to put together a calendar of cardio workouts for the year. I would have 4 different workouts per week + 2 basic steady state workouts. I envision a picture of me on the top page and along with the challenge of the month description and the 3 different types of cardio description. on the bottom page would be the calendar for that month with the workout typed into the box. I am not sure if a boxed calendar would be enough space to write each workout in so I am open to more ideas on how to present the workouts

Target Market(s)

Women 20-60 years old
moms
couples
men
athletes

Industry/Entity Type

Fitness

Font styles to use
Sans Serif

Colors

Designer to choose colors to be used in the design.

Requirements
Must have
• Ability to incorporate 4 different workouts per week in a downloadable calendar style
• I want to have a different picture available for each month
• modern, bold, but simple and clean presentation
Nice to have
• picture at the top, with a description of the 3 different types of workouts for that month.
• On the bottom would be space for separate days of each workout
Should not have
• NA

```html
<!DOCTYPE html>
<html lang="en">
<head>
<meta charset="utf-8">
<title>Ignite a Hidden Titan Within – January 2019</title>
<link href="https://fonts.googleapis.com/css2?family=Exo+2:wght@200;300&family=Roboto+Condensed:wght@400&display=swap" rel="stylesheet">
<style>
  :root {
    --page-bg: #0a0b0d;
    --ink: #ffffff;
    --accent: #e0060b;
    --rule: #a4060a;
    --header-navy: #0d1a26;
    --field-green: #1f3a1c;
  }
  * { margin: 0; padding: 0; box-sizing: border-box; }
  html, body { width: 844px; height: 1200px; overflow: hidden; background: var(--page-bg); }
  .page {
    position: relative; width: 844px; height: 1200px;
    background: var(--page-bg); color: var(--ink);
    font-family: "Exo 2", sans-serif; font-weight: 300;
  }
  .hero-photo {
    position: absolute; left: 0; top: 0; width: 844px; height: 520px;
    background:
      linear-gradient(180deg, transparent 0%, transparent 70%, var(--page-bg) 100%),
      linear-gradient(180deg, var(--header-navy) 0%, #0b1119 32%, #0c0f12 62%, var(--field-green) 82%, #15261a 90%);
  }
  .challenge {
    position: absolute; left: 0; top: 36px; width: 844px; text-align: center;
  }
  .challenge-title { font-size: 38px; font-weight: 300; letter-spacing: 0.5px; line-height: 1; }
  .challenge-text {
    width: 650px; margin: 16px auto 0;
    font-family: "Roboto Condensed", sans-serif; font-size: 10px; line-height: 13.6px;
  }
  .month-title {
    position: absolute; left: 64px; top: 548px;
    font-size: 40px; font-weight: 300; line-height: 1;
  }
  .calendar {
    position: absolute; left: 64px; top: 644px; width: 714px;
    display: grid;
    grid-template-columns: 94px 113px 103px 116px 108px 90px 90px;
    grid-template-rows: 63px 51px 51px 51px 52px 47px;
  }
  .calendar > div {
    display: flex; align-items: center; justify-content: center;
    border-right: 1px solid var(--rule); border-bottom: 1px solid var(--rule);
    font-size: 24px;
  }
  .calendar > div:nth-child(7n) { border-right: none; }
  .calendar > div:nth-last-child(-n+7) { border-bottom: none; }
  .calendar .weekday { color: var(--accent); font-size: 35px; padding-top: 2px; }
  .workouts {
    position: absolute; left: 70px; top: 1018px;
    list-style: none; font-size: 37px; line-height: 48px; letter-spacing: 0.6px;
  }
</style>
</head>
<body>
<main class="page">
  <div class="hero-photo" role="img" aria-label="Athlete in a tank top and red leggings using a foam roller on a dark turf field"></div>

  <header class="challenge">
    <h1 class="challenge-title">Challenge of the month</h1>
    <p class="challenge-text">Lorem ipsum dolor sit amet, consectetur adipiscing elit. Nam lobortis magna ut libero feugiat, euismod commodo risus scelerisque. Suspendisse fermentum risus ut fermentum porttitor. Vivamus dolor mauris, fermentum non augue placerat, cursus pellentesque ex. Praesent consequat feugiat convallis. Proin tristique nisi justo, sed aliquam felis egestas malesuada. Aliquam orci quam, vulputate sit amet neque non, feugiat porttitor ligula. Fusce congue maximus sagittis. Interdum et malesuada fames ac ante</p>
  </header>

  <h2 class="month-title">January - 2019</h2>

  <section class="calendar">
    <div class="weekday">Sun</div><div class="weekday">Mon</div><div class="weekday">Tue</div><div class="weekday">Wed</div><div class="weekday">Thu</div><div class="weekday">Fri</div><div class="weekday">Sat</div>
    <div>30</div><div>31</div><div>1</div><div>2</div><div>3</div><div>4</div><div>5</div>
    <div>6</div><div>7</div><div>8</div><div>9</div><div>10</div><div>11</div><div>12</div>
    <div>13</div><div>14</div><div>15</div><div>16</div><div>17</div><div>18</div><div>19</div>
    <div>20</div><div>21</div><div>22</div><div>23</div><div>24</div><div>25</div><div>26</div>
    <div>27</div><div>28</div><div>29</div><div>30</div><div>31</div><div></div><div></div>
  </section>

  <ul class="workouts">
    <li>Cardio Excercise #1</li>
    <li>Cardio Excercise #2</li>
    <li>Cardio Excercise #3</li>
  </ul>
</main>
</body>
</html>
```